New Toothpaste brand needs a logo & packaging design

Our company is launching a new toothpaste and is looking for a logo and packaging design. The toothpaste brand is called Brivana. The packaging should have the same design quality as the major international brands, such as Lumora, Lumora Totalcare, Dentiva, Pexolo, Wind-rise, Marvest, etc. The dominant colors for our brand should be hues of blue, similar to other major brands. In addition, there should be a little bit of green to represent the "Fresh Mint Blast" flavor and the "Extracts of Aloe Vera" included in the ingredients.

There are typically 3 unique sides on a toothpaste box:

The face: Repeated on ~3 sides of the 4 faces of the box
The back: The 4th box face has the instructions for use, ingredients, company information, bar code/product info, and some branding elements.
The sides: Usually consisting of just the logo, flavor etc.

Please refer to existing brands such as Lumora, Lumora Total-care, and Dentiva for an example of typical box layout and elements.

Task Details:
Package Dimensions: 180 mm x 48 mm x 28 mm, 100 ml toothpaste tube
Brand Name: Brivana
Description: Fluoride Toothpaste
Flavor: Fresh Mint Blast
5 Actions: Protects against cavities and tartar, freshens breath, whitens teeth, and maintains healthy gums. These actions can also be made into a list like Lumora Total Care or Dentiva Max care. For instance, Strong Teeth, Fresh Breath, Whitening, Healthy Gums, Cavity and Tartar Protection.
Also contains whitening micro particles and extracts of aloe vera which may be highlighted on the package

Overall, the look should be high quality and with the same look and feel as the big brands mentioned previously. We do not have an existing logo for this brand. The face of the package is the most important element as it is often repeated on several sides and on the tube itself.

Please let me know if you have any questions.

I've attached some of our favorite big brand designs below. I would say the Lumora Total Care and Gleam vers

The logos I've seen so far for Brivana, have been a bit too bold. A little bold is okay, but just needs to be moderate. 

I would like the colors to be bright and appealing. I mentioned shades of blue being the major color, but green should also be highlighted as well, perhaps in a 80% blue to 20% green ratio. 

Target Market(s)

adult consumer of toothpaste, both female and male.

Industry/Entity Type

It Company

Requirements
Must have
• A logo with the brand name: Brivana
Description or sub text: Fluoride Toothpaste
Flavor: Fresh Mint Blast
A phrase or list describing the Toothpaste Actions: e.g., Protects against cavities and tartar, freshens breath, whitens teeth, and maintains healthy gums. Or as a list simialr to Lumora Total Care or Dentiva Max Care:
-Anti-cavity
-Anti-tartar
-Fresh breath
-Whitening
-Healthy Gums

Special ingredient of "whitening micro particles: and "extracts of aloe vera", which should also be highlighted.

The color should mostly be shades of blue, with only a little bit of green to accentuate the fresh mint blast flavor and aloe vera

Nice to have
• The design should really look good next to lumora total care, gleam pure, and dentiva max care. These are our favorite designs.
Should not have
• For aloe vera, there is no need to show the plant.

The Brivana logo shouldn't be too Bold. This should be appeal to all consumers, not just men.

```html
<!DOCTYPE html>
<html lang="en">
<head>
<meta charset="utf-8">
<title>Brivana Fluoride Toothpaste – Box Panels</title>
<link rel="stylesheet" href="https://fonts.googleapis.com/css2?family=Open+Sans:wght@400;600;700&family=Tinos:wght@400;700&display=swap">
<style>
  :root {
    --page-bg: #eceef1;
    --box-blue-deep: #0a4fb8;
    --box-blue: #1d7fe0;
    --box-blue-light: #6fc0ff;
    --band-cyan: #14e0f0;
    --band-cyan-deep: #00a9e6;
    --mint-green: #22d63c;
    --mint-green-deep: #0a8a1e;
    --aloe-text: #9dff6a;
    --aloe-strip: #f2fff0;
    --accent-red: #c8102e;
    --text-white: #ffffff;
    --flavour-black: #050a10;
  }
  * { margin: 0; padding: 0; box-sizing: border-box; }
  html, body {
    width: 1200px;
    height: 946px;
    overflow: hidden;
    background: var(--page-bg);
  }
  .canvas {
    position: relative;
    width: 1200px;
    height: 946px;
    font-family: "Open Sans", sans-serif;
    color: var(--text-white);
  }
  .panel {
    position: absolute;
    overflow: hidden;
    background: linear-gradient(180deg, var(--box-blue) 0%, var(--box-blue-deep) 100%);
  }
  .panel-art {
    position: absolute;
    inset: 0;
    width: 100%;
    height: 100%;
  }

  /* ---------- top panel ---------- */
  .top-panel {
    left: 45px;
    top: 270px;
    width: 960px;
    height: 149px;
    background: linear-gradient(180deg, var(--box-blue-deep) 0%, var(--box-blue) 100%);
  }
  .top-panel .brand-name {
    position: absolute;
    left: 40px;
    top: 42px;
    font-size: 46px;
    font-weight: 600;
    line-height: 1;
    letter-spacing: -1px;
  }
  .top-panel .product-type {
    position: absolute;
    left: 300px;
    top: 52px;
    font-family: "Tinos", serif;
    font-size: 16px;
    line-height: 1.05;
    text-transform: uppercase;
  }
  .top-panel .headline {
    position: absolute;
    left: 470px;
    top: 34px;
    font-size: 34px;
    font-weight: 400;
    white-space: nowrap;
  }
  .top-panel .ingredient {
    position: absolute;
    left: 700px;
    top: 104px;
    width: 260px;
    height: 26px;
    line-height: 26px;
    padding-left: 22px;
    font-size: 16px;
    font-weight: 600;
    color: var(--mint-green-deep);
  }

  /* ---------- front panel ---------- */
  .front-panel {
    left: 45px;
    top: 419px;
    width: 960px;
    height: 256px;
  }
  .new-flag {
    position: absolute;
    left: 16px;
    top: 10px;
    font-size: 28px;
    font-weight: 700;
    line-height: 1;
    color: var(--accent-red);
  }
  .front-panel .brand-name {
    position: absolute;
    left: 30px;
    top: 62px;
    font-size: 62px;
    font-weight: 600;
    line-height: 1;
    letter-spacing: -1.5px;
  }
  .front-panel .product-type {
    position: absolute;
    left: 162px;
    top: 158px;
    font-family: "Tinos", serif;
    font-size: 19px;
    line-height: 1.02;
    text-transform: uppercase;
  }
  .volume {
    position: absolute;
    left: 16px;
    top: 198px;
    font-family: "Tinos", serif;
    font-size: 14px;
  }
  .front-panel .headline {
    position: absolute;
    left: 322px;
    top: 32px;
    font-size: 36px;
    font-weight: 400;
    white-space: nowrap;
  }
  .front-panel .ingredient {
    position: absolute;
    left: 636px;
    top: 108px;
    font-size: 17px;
    font-weight: 600;
    line-height: 22px;
    color: var(--aloe-text);
  }
  .benefits {
    position: absolute;
    left: 330px;
    top: 148px;
    display: flex;
    gap: 6px;
    list-style: none;
    font-size: 12.5px;
    font-weight: 700;
    text-transform: uppercase;
    white-space: nowrap;
  }
  .benefits li + li::before {
    content: "•";
    margin-right: 6px;
  }
  .flavour {
    position: absolute;
    right: 0;
    top: 218px;
    width: 186px;
    height: 28px;
    background: var(--flavour-black);
    font-family: "Tinos", serif;
    font-weight: 700;
    font-size: 16px;
    line-height: 28px;
    text-align: center;
    text-transform: uppercase;
  }

  /* ---------- end panel ---------- */
  .end-panel {
    left: 1005px;
    top: 419px;
    width: 149px;
    height: 256px;
    background: linear-gradient(90deg, var(--box-blue-deep) 0%, var(--box-blue) 100%);
  }
  .end-panel .brand-name {
    position: absolute;
    left: 50%;
    top: 96px;
    transform: translate(-50%, -50%) rotate(90deg);
    font-size: 40px;
    font-weight: 600;
    line-height: 1;
    letter-spacing: -1px;
    white-space: nowrap;
  }
</style>
</head>
<body>
<main class="canvas">

  <section class="panel top-panel" aria-label="Brivana toothpaste box, top panel">
    <svg class="panel-art" viewBox="0 0 960 149" aria-hidden="true">
      <defs>
        <linearGradient id="top-glow" x1="0" y1="0" x2="1" y2="0">
          <stop offset="0" stop-color="var(--box-blue-light)" stop-opacity="0.1"/>
          <stop offset="1" stop-color="var(--box-blue-light)" stop-opacity="0.5"/>
        </linearGradient>
      </defs>
      <path d="M430 0 H960 V149 H500 C470 110 460 50 430 0 Z" fill="url(#top-glow)"/>
      <rect x="700" y="104" width="260" height="26" fill="var(--aloe-strip)"/>
      <rect x="700" y="130" width="260" height="5" fill="var(--mint-green)"/>
    </svg>
    <p class="brand-name">Brivana</p>
    <p class="product-type">Fluoride<br>Toothpaste</p>
    <p class="headline">whitening micro particles</p>
    <p class="ingredient">aloe vera extracts</p>
  </section>

  <section class="panel front-panel" aria-label="Brivana toothpaste box, front panel">
    <svg class="panel-art" viewBox="0 0 960 256" aria-hidden="false">
      <defs>
        <linearGradient id="wave-light" x1="0" y1="0" x2="1" y2="0">
          <stop offset="0" stop-color="var(--box-blue-light)" stop-opacity="0.55"/>
          <stop offset="1" stop-color="var(--box-blue-light)" stop-opacity="0.15"/>
        </linearGradient>
        <linearGradient id="band-cyan" x1="0" y1="0" x2="1" y2="0">
          <stop offset="0" stop-color="var(--band-cyan-deep)"/>
          <stop offset="0.5" stop-color="var(--band-cyan)"/>
          <stop offset="1" stop-color="var(--band-cyan)"/>
        </linearGradient>
        <linearGradient id="band-green" x1="0" y1="0" x2="1" y2="0">
          <stop offset="0" stop-color="var(--mint-green-deep)"/>
          <stop offset="0.4" stop-color="var(--mint-green)"/>
          <stop offset="1" stop-color="var(--mint-green)"/>
        </linearGradient>
        <linearGradient id="dot-field" x1="0" y1="0" x2="1" y2="0">
          <stop offset="0" stop-color="#ffffff" stop-opacity="0.9"/>
          <stop offset="0.45" stop-color="#9fd0ff" stop-opacity="0.7"/>
          <stop offset="1" stop-color="var(--box-blue-deep)" stop-opacity="0.4"/>
        </linearGradient>
        <linearGradient id="mint-streak" x1="0" y1="0" x2="1" y2="0">
          <stop offset="0" stop-color="var(--mint-green)" stop-opacity="0"/>
          <stop offset="0.5" stop-color="var(--mint-green)"/>
          <stop offset="1" stop-color="var(--aloe-text)"/>
        </linearGradient>
      </defs>
      <path class="wave-highlight" d="M300 0 H960 V134 H470 C410 134 390 100 365 62 C345 32 322 14 300 0 Z" fill="url(#wave-light)"/>
      <rect class="aloe-band" x="560" y="108" width="400" height="24" fill="url(#band-green)"/>
      <path class="benefit-band" d="M415 134 H960 V184 H480 C450 184 430 160 415 134 Z" fill="url(#band-cyan)"/>
      <path class="dot-field" role="img" aria-label="Halftone dot texture suggesting whitening micro particles"
            d="M340 214 C400 198 445 186 500 184 H960 V256 H420 C385 240 360 228 340 214 Z" fill="url(#dot-field)"/>
      <rect x="500" y="198" width="460" height="5" fill="url(#mint-streak)"/>
      <rect x="540" y="209" width="420" height="4" fill="url(#mint-streak)"/>
    </svg>

    <span class="new-flag">new</span>
    <h1 class="brand-name">Brivana</h1>
    <p class="product-type">Fluoride<br>Toothpaste</p>
    <p class="volume">100ml</p>

    <h2 class="headline">whitening micro particles</h2>
    <p class="ingredient">aloe vera extracts</p>
    <ul class="benefits">
      <li>Anti cavity</li>
      <li>Anti tartar</li>
      <li>Fresh breath</li>
      <li>Whitening</li>
      <li>Healthy gums</li>
    </ul>
    <p class="flavour">Fresh Mint Blast</p>
  </section>

  <section class="panel end-panel" aria-label="Brivana toothpaste box, end panel">
    <svg class="panel-art" viewBox="0 0 149 256" aria-hidden="true">
      <defs>
        <linearGradient id="end-cyan" x1="0" y1="0" x2="1" y2="0">
          <stop offset="0" stop-color="var(--band-cyan-deep)"/>
          <stop offset="1" stop-color="var(--band-cyan)"/>
        </linearGradient>
      </defs>
      <rect x="0" y="108" width="149" height="24" fill="var(--mint-green)"/>
      <rect x="0" y="134" width="149" height="50" fill="url(#end-cyan)"/>
      <rect x="0" y="218" width="149" height="28" fill="var(--flavour-black)"/>
    </svg>
    <p class="brand-name">Brivana</p>
  </section>

</main>
</body>
</html>
```